Web Design Project

We are re-starting this project.

This project is for a totally new look and design of a website for Wozzlent. www.wozzlent-example.com.

Wozzlent is a naming protocol for physical locations and can be used for fixed and mobile people, places and things. Find your friends, or find a business. Because Wozzlent locations point to precise geo-physical (GPS) co-ordinates, navigation to a location becomes totally reliable.
Updates

Please see the modified brief for this project

Target Market(s)

Every person and every business can have multiple !Wozzs (Wozzlent locations), so the website needs to be appealing and fun, but easy to use and functional

Industry/Entity Type

Business

Colors
34a6d7

Requirements
Must have
• Uniqueness!

```html
<!DOCTYPE html>
<html lang="en">
<head>
<meta charset="utf-8">
<title>Wozzlent</title>
<link href="https://fonts.googleapis.com/css2?family=Arimo:wght@400;700&display=swap" rel="stylesheet">
<style>
  :root {
    --brand: #34a6d7;
    --brand-dark: #1f86b4;
    --ink: #222222;
    --muted: #444444;
    --rule: #9a9a9a;
    --field: #ececec;
    --white: #ffffff;
  }
  * { box-sizing: border-box; margin: 0; padding: 0; }
  html, body { width: 1200px; height: 769px; overflow: hidden; background: var(--white); }
  body { position: relative; font-family: "Arimo", Arial, sans-serif; color: var(--ink); }

  .top-band { position: absolute; left: 0; top: 0; width: 1200px; height: 7px; background: var(--brand); }

  .brand { position: absolute; left: 123px; top: 34px; display: flex; align-items: center; gap: 10px; }
  .brand-dot { width: 22px; height: 22px; border-radius: 50%; background: var(--brand); }
  .brand-name { font-size: 50px; font-weight: 700; color: var(--brand); letter-spacing: -1px; line-height: 1; }

  .account-nav { position: absolute; right: 121px; top: 50px; display: flex; align-items: center; font-size: 12px; font-weight: 700; }
  .account-nav a { color: var(--muted); text-decoration: none; }
  .account-nav .divider { width: 1px; height: 13px; background: #999; margin: 0 14px 0 11px; }

  .hero { position: absolute; left: 120px; top: 107px; width: 960px; height: 562px; overflow: hidden; }
  .hero-photo { position: absolute; inset: 0;
    background:
      radial-gradient(ellipse 70% 40% at 50% 72%, rgba(190,90,30,0.55), transparent 70%),
      linear-gradient(180deg, #050403 0%, #120a05 28%, #3a1f0c 48%, #4a2810 62%, #2a160a 80%, #0c0704 100%); }
  .search { position: absolute; left: 213px; top: 253px; width: 534px; height: 56px; background: var(--brand); padding: 8px 6px; display: flex; gap: 7px; }
  .search-field { width: 408px; height: 40px; background: var(--field); border: 1px solid #c9c9c9; font: 400 17px "Arimo", Arial, sans-serif; color: #444; padding: 0 13px; display: flex; align-items: center; }
  .search-button { width: 104px; height: 40px; background: linear-gradient(180deg, #3fb1e0, var(--brand-dark)); border: 1px solid #1a75a0; color: var(--white); font: 400 17px "Arimo", Arial, sans-serif; display: flex; align-items: center; justify-content: center; }
  .hero-caption { position: absolute; left: 0; bottom: 0; width: 960px; height: 73px; background: linear-gradient(180deg, rgba(0,0,0,0.35), rgba(0,0,0,0.75)); display: flex; align-items: center; justify-content: center; gap: 14px; color: var(--white); font-size: 17px; padding-top: 2px; }
  .hero-caption .places { font-size: 19px; }
  .hero-caption a { color: var(--brand); text-decoration: none; }

  .footer-rule { position: absolute; left: 0; top: 714px; width: 1200px; height: 1px; background: var(--rule); }
  .footer-nav { position: absolute; left: 123px; top: 733px; display: flex; gap: 15px; font-size: 13.5px; }
  .footer-nav a { color: var(--ink); text-decoration: none; }
  .powered { position: absolute; right: 121px; top: 735px; font-size: 11.5px; color: var(--brand); }
  .corner-mark { position: absolute; left: 1176px; top: 735px; font-size: 12px; color: var(--ink); }
</style>
</head>
<body>
  <div class="top-band"></div>

  <header>
    <div class="brand">
      <span class="brand-dot"></span>
      <span class="brand-name">Wozzlent</span>
    </div>
    <nav class="account-nav">
      <a href="#">SIGN UP</a>
      <span class="divider"></span>
      <a href="#">LOGIN</a>
    </nav>
  </header>

  <section class="hero">
    <div class="hero-photo" role="img" aria-label="Night-time city skyline with lit skyscrapers beside a harbour"></div>
    <form class="search">
      <div class="search-field">Who would you like to find?</div>
      <div class="search-button">Search</div>
    </form>
    <div class="hero-caption">
      <span>Wozzlent lets you store specific locations such as <span class="places">Home, Work, Fish.</span></span>
      <a href="#">Update Your Location Now</a>
    </div>
  </section>

  <div class="footer-rule"></div>
  <footer>
    <nav class="footer-nav">
      <a href="#">ABOUT</a><a href="#">HELP</a><a href="#">CONTACT</a><a href="#">PRIVACY</a><a href="#">TERMS</a><a href="#">REFUNDS</a><a href="#">FAQ</a>
    </nav>
    <div class="powered">POWERED BY WOZZLENT API</div>
    <div class="corner-mark">X7</div>
  </footer>
</body>
</html>
```